Small Business Broker Business Card Design

A business card design for a small business brokerage, which is a financial service, not unlike real estate brokerage, but for small businesses such as laundromats, pizza shops, restaurants, cleaners etc. The designs should all be simple, more conservative in nature, using the colors and font of the logo. Again, think real estate Brokerage as a business context
Contact Information for Business Card
Name: Dale R. Whitmore. Title: Small Business Advisor. Email: d.whitmore@lanternbridgeadvisory.com. Mobile: (917) 555-0148. Office: (718) 555-0193. www.lanternbridgeadvisory.com

```html
<!DOCTYPE html>
<html lang="en">
<head>
<meta charset="utf-8">
<title>Lanternbridge Advisory – Business Card</title>
<link rel="stylesheet" href="https://fonts.googleapis.com/css2?family=Montserrat:wght@600;700&family=Open+Sans:wght@400;700&display=swap">
<style>
  :root {
    --navy: #1d3a6b;
    --green: #8cc63f;
    --ink: #111111;
    --paper: #ffffff;
    --backdrop: #9a9a9a;
    --faint-navy: rgba(29, 58, 107, 0.13);
    --faint-green: rgba(140, 198, 63, 0.14);
  }
  * { margin: 0; padding: 0; box-sizing: border-box; }
  html, body {
    width: 1200px;
    height: 1200px;
    overflow: hidden;
    background: var(--backdrop);
  }
  .card {
    position: absolute;
    left: 226px;
    width: 746px;
    height: 436px;
    overflow: hidden;
  }
  /* Front side */
  .card-front { top: 100px; }
  .front-field {
    position: absolute;
    inset: 0;
    background: linear-gradient(90deg, var(--navy) 0%, var(--navy) 36%, #4f7f5a 54%, var(--green) 70%, var(--green) 100%);
  }
  .front-brand {
    position: absolute;
    right: 46px;
    bottom: 64px;
    display: flex;
    align-items: center;
    gap: 10px;
    color: var(--paper);
    font-family: "Montserrat", sans-serif;
    font-weight: 700;
    font-size: 15px;
    letter-spacing: 0.08em;
  }
  .front-brand .brand-square {
    width: 22px;
    height: 22px;
    background: var(--paper);
  }
  /* Back side */
  .card-back { top: 612px; background: var(--paper); }
  .back-decoration {
    position: absolute;
    left: 361px;
    top: 144px;
    width: 385px;
    height: 292px;
    background: linear-gradient(100deg, rgba(255,255,255,0) 0%, var(--faint-green) 45%, var(--faint-navy) 100%);
    clip-path: polygon(35% 0, 100% 22%, 100% 100%, 0 100%);
  }
  .brand-lockup {
    position: absolute;
    left: 95px;
    top: 46px;
    display: flex;
    align-items: center;
    gap: 18px;
  }
  .brand-lockup .brand-square {
    width: 72px;
    height: 72px;
    background: var(--navy);
  }
  .brand-name {
    font-family: "Montserrat", sans-serif;
    font-weight: 700;
    font-size: 24px;
    letter-spacing: 0.04em;
    color: var(--navy);
    text-transform: uppercase;
    line-height: 1.1;
  }
  .brand-tagline {
    margin-top: 5px;
    font-family: "Montserrat", sans-serif;
    font-weight: 600;
    font-size: 12.5px;
    letter-spacing: 0.13em;
    color: var(--green);
    text-transform: uppercase;
  }
  .contact {
    position: absolute;
    left: 97px;
    top: 178px;
    font-family: "Open Sans", sans-serif;
    color: var(--ink);
  }
  .person-name {
    font-family: "Montserrat", sans-serif;
    font-weight: 700;
    font-size: 24px;
    letter-spacing: 0.04em;
    color: var(--navy);
    text-transform: uppercase;
    line-height: 1.1;
  }
  .person-title {
    font-family: "Montserrat", sans-serif;
    font-weight: 600;
    font-size: 12.5px;
    letter-spacing: 0.06em;
    color: var(--green);
    text-transform: uppercase;
    margin-top: 3px;
  }
  .contact-line { font-size: 19.5px; line-height: 24px; }
  .contact-email { margin-top: 22px; }
  .contact-phones { margin-top: 25px; }
  .contact-web { margin-top: 25px; }
  .contact strong { font-weight: 700; }
</style>
</head>
<body>
  <section class="card card-front">
    <div class="front-field" role="img" aria-label="Navy to green gradient field with repeating brand pattern"></div>
    <div class="front-brand"><span class="brand-square"></span>LANTERNBRIDGE</div>
  </section>

  <section class="card card-back">
    <div class="back-decoration" role="img" aria-label="Faint large brand decoration"></div>
    <header class="brand-lockup">
      <span class="brand-square"></span>
      <div>
        <div class="brand-name">Lanternbridge Advisory, Inc</div>
        <div class="brand-tagline">Trusted guidance for every business transition</div>
      </div>
    </header>
    <div class="contact">
      <div class="person-name">Dale R. Whitmore</div>
      <div class="person-title">Small Business Advisor</div>
      <div class="contact-line contact-email">d.whitmore@lanternbridgeadvisory.com</div>
      <div class="contact-phones">
        <div class="contact-line"><strong>Mobile:</strong> (917) 555-0148</div>
        <div class="contact-line"><strong>Office:</strong> (718) 555-0193</div>
      </div>
      <div class="contact-line contact-web"><strong>www.lanternbridgeadvisory</strong>.com</div>
    </div>
  </section>
</body>
</html>
```